Stationary (Business Cards, envelopes, cover letters, etc) for HARBOR LANTERN PARTNERS
The Harbor Lantern Partners
Stationary (Business Cards, envelopes, cover letters, etc) for HARBOR LANTERN PARTNERS - Business Opportunities
Creative Brief
Professional
Rodrigo Velasco Brennan
Av. Ignacio Marroquín 718 B Col. Los Pinos Altos México DF CP 01482 México
rvelasco@hlp-example.mx
www.hlp-example.mx
First impressions have high impact, so in terms of the business card, it has to be something that's out of the box. The card is used to present ourselves to another party or prospect, but it also has to have a high impact message, either by an image or a phrase that comes attached in the back side. It could be some key points of a preview success case. So the back side has to have a marketing application. It has to be a card that will stand out, so much that it will be shown and passed around. In design and in materials (maybe???), although win the materials it will have a high impact on the costs of production. It has to be standard size, so it fits in every wallet thus avoiding on being thrown somewhere.
Concepts
Business Card and Stationary Project for a multifaceted corporation
Stationary for holding company
Business cards for RFTV - Investimentos e Administrações
mitiha mitiha
GREAT NEWS! WE'VE EXTENDED TO THIS FRIDAY! KEEP UP THE GREAT WORK!!!
Hi designers! GREAT JOB! We are want to decide today (our time) the winner. Please if you have any questions, let us know. Try to show as much applications as possible, i.e. we're now in a digital world so some digital applications we'll be considered for higher points. Have seen proposals in blue and gray (predominant colors and mixed), but none in orange. Let's see some! *Don't use curved lines in your design proposals. THANKS!
Hi, first of all I want to thank each and every one of you for accepting in working on our project. GREAT DESIGNS !!!!! Something we don't want is the lines that make a "curve" to separate content. I've seen a lot of those in the market and we want to be ORIGINAL. As I said in the brief, we want our cards to be saved as something awsome, and to be shown to other people. Material: sent your proposals of other materials, however if you can also send the specificatiosn of that material so we can see the cost of printing in them. Remember that it's not only the business cards but the stationary. KEEP UP THE GREAT JOB! CREATE DESIGN!

```html
<!DOCTYPE html>
<html lang="en">
<head>
<meta charset="utf-8">
<title>Harbor Lantern Partners – Business Card</title>
<link href="https://fonts.googleapis.com/css2?family=Cinzel:wght@600&family=Open+Sans:wght@400;600&display=swap" rel="stylesheet">
<style>
  :root {
    --bg: #e4e5e7;
    --card: #ffffff;
    --dark: #2a2b2d;
    --blue: #1b8fd8;
    --orange: #ee7d2b;
    --ink: #3a3a3c;
    --rule: #9a9a9c;
    --light: #f2f2f2;
    --muted: #c9c9c9;
    --soft: #7a7b7e;
  }
  * { box-sizing: border-box; margin: 0; padding: 0; }
  html, body { width: 1200px; height: 901px; overflow: hidden; }
  body {
    background: var(--bg);
    font-family: "Open Sans", Arial, sans-serif;
    position: relative;
  }
  .card {
    position: absolute;
    left: 320px;
    width: 560px;
    height: 320px;
    background: var(--card);
    border-radius: 14px;
    overflow: hidden;
    box-shadow: 0 6px 18px rgba(0,0,0,.18);
  }
  .card--back { top: 110px; }
  .card--front { top: 470px; }

  /* Brand block: square, rule, name, rule */
  .brand {
    display: flex;
    flex-direction: column;
    align-items: center;
    text-align: center;
  }
  .brand__mark {
    width: 22px; height: 22px;
    background: var(--orange);
    margin-bottom: 12px;
  }
  .brand__rule {
    width: 100%;
    height: 1px;
    background: var(--rule);
  }
  .brand__name {
    font-family: "Cinzel", Georgia, serif;
    font-weight: 600;
    font-size: 16px;
    line-height: 1.3;
    letter-spacing: .06em;
    color: var(--ink);
    padding: 6px 0;
  }

  .card--back .brand {
    position: absolute;
    left: 50%; top: 96px;
    width: 230px;
    transform: translateX(-50%);
  }
  .back__message {
    position: absolute;
    left: 0; right: 0;
    top: 232px;
    text-align: center;
    font-size: 10px;
    letter-spacing: .18em;
    text-transform: uppercase;
    color: var(--soft);
  }

  .front__art { position: absolute; inset: 0; }
  .card--front .brand {
    position: absolute;
    left: 50px; top: 96px;
    width: 210px;
  }

  .contact {
    position: absolute;
    right: 22px;
    top: 30px;
    width: 190px;
    color: var(--light);
    text-align: right;
  }
  .contact__name {
    font-size: 11px;
    font-weight: 600;
    letter-spacing: .04em;
    text-transform: uppercase;
    white-space: nowrap;
  }
  .contact__role {
    font-size: 8px;
    letter-spacing: .12em;
    text-transform: uppercase;
    color: var(--muted);
    margin-top: 2px;
  }
  .contact__address {
    font-size: 8.5px;
    line-height: 1.5;
    margin-top: 26px;
  }
  .contact__list { list-style: none; margin-top: 22px; }
  .contact__item {
    display: flex;
    justify-content: flex-end;
    align-items: center;
    gap: 7px;
    font-size: 8px;
    line-height: 1;
    margin-bottom: 10px;
  }
  .contact__item svg { width: 9px; height: 9px; flex: none; fill: var(--light); }
</style>
</head>
<body>

  <section class="card card--back" aria-label="Card back">
    <div class="brand">
      <span class="brand__mark"></span>
      <span class="brand__rule"></span>
      <span class="brand__name">The Harbor Lantern<br>Partners</span>
      <span class="brand__rule"></span>
    </div>
    <p class="back__message">Turning opportunities into growth</p>
  </section>

  <section class="card card--front" aria-label="Card front">
    <svg class="front__art" viewBox="0 0 560 320" aria-hidden="true">
      <polygon fill="var(--blue)" points="330,0 560,0 560,320 296,320"/>
      <polygon fill="var(--dark)" points="344,0 560,0 560,320 310,320"/>
    </svg>

    <div class="brand">
      <span class="brand__mark"></span>
      <span class="brand__rule"></span>
      <span class="brand__name">The Harbor Lantern<br>Partners</span>
      <span class="brand__rule"></span>
    </div>

    <div class="contact">
      <p class="contact__name">Rodrigo Velasco Brennan</p>
      <p class="contact__role">President</p>
      <p class="contact__address">Av. Ignacio Marroquín 718 B<br>Col. Los Pinos Altos</p>
      <ul class="contact__list">
        <li class="contact__item">012 555 0147
          <svg viewBox="0 0 10 10"><path d="M2,0.5 L3.5,0.5 L4.2,2.8 L3,3.6 C3.6,5 5,6.4 6.4,7 L7.2,5.8 L9.5,6.5 L9.5,8 C9.5,9 8.8,9.5 8,9.5 C4,9.2 0.8,6 0.5,2 C0.5,1.2 1,0.5 2,0.5 Z"/></svg>
        </li>
        <li class="contact__item">012 555 0148
          <svg viewBox="0 0 10 10"><path d="M3,0 H7 A1,1 0 0 1 8,1 V9 A1,1 0 0 1 7,10 H3 A1,1 0 0 1 2,9 V1 A1,1 0 0 1 3,0 Z M3,1.5 V7.5 H7 V1.5 Z"/></svg>
        </li>
        <li class="contact__item">012 555 0149
          <svg viewBox="0 0 10 10"><path d="M2.5,0.5 H7.5 V3 H9.5 V7.5 H7.5 V9.5 H2.5 V7.5 H0.5 V3 H2.5 Z M3.5,6 V8.5 H6.5 V6 Z"/></svg>
        </li>
        <li class="contact__item">rvelasco@hlp-example.mx
          <svg viewBox="0 0 10 10"><path d="M0.5,2 H9.5 V8 H0.5 Z M1.2,2.6 L5,5.6 L8.8,2.6 Z"/></svg>
        </li>
        <li class="contact__item">www.hlp-example.mx
          <svg viewBox="0 0 10 10"><path d="M5,0.5 A4.5,4.5 0 1 0 5,9.5 A4.5,4.5 0 1 0 5,0.5 Z M5,1.5 C6,2.5 6.4,3.6 6.4,5 C6.4,6.4 6,7.5 5,8.5 C4,7.5 3.6,6.4 3.6,5 C3.6,3.6 4,2.5 5,1.5 Z"/></svg>
        </li>
      </ul>
    </div>
  </section>

</body>
</html>
```